Online radio: TunaWave homepage redesign

TunaWave is one of the world's leading brands of personalizable online radio -- similar to Melodex, but aimed at a somewhat older audience (age 35-54).

We'd like to redesign our homepage with a more contemporary look: It should emphasize our wide variety of GENRES (as the primary navigation), with the search field easy to find as a secondary navigation.

We'd like to retain our corporate color of maroon/plum. (We are not committed to the gold/yellow secondary color.)

See our current homepage at www.tunawave-example.com and our in-house attempt at an improved design at http://web4.tunawave-example.com/finder/2013ms/.

Ideally, we'd like to see designs for up to THREE different states:

(1) An initial state when users first come to the page.

(2) What the page would look like as the user is looking at channel options.

(3) What the page would look like once the media player is launched.

However, you may be able to combine (2) and (3) in a single screenshot.

Thanks!
Updates

At the request of several designers, we have decided to extend our deadline by four days. At the same time, we have increased our budget, including the addition of a 2nd place award. Thanks for your excellent work!

Thanks very much for your designs! We are very pleased with the overall quality of the work we are seeing. One reminder: As our brief says, the user interface "should emphasize our wide variety of GENRES (as the primary navigation), with the search field easy to find as a secondary navigation," and we feel that your design uses the SEARCH field as the primary navigation. Many of the designs use a large search field as the primary navigation. If yours does, you might want to tweak your design to put a greater emphasis on browsing genres as the primary navigation. Thanks and good luck!

Target Market(s)

Adults age 35-54 listening to online radio at work

Industry/Entity Type

Radio

Font styles to use
Sans Serif

Requirements
Must have
• This is a design/UI project -- we do not need code

```html
<!DOCTYPE html>
<html lang="en">
<head>
<meta charset="utf-8">
<title>TunaWave – Online Radio</title>
<link href="https://fonts.googleapis.com/css2?family=Roboto:wght@400;500&display=swap" rel="stylesheet">
<style>
:root{
  --plum:#5e0f5e;
  --plum-dark:#3a063a;
  --plum-light:#8a2a8a;
  --gold:#f6c500;
  --page:#c9c9c9;
  --panel:#333;
  --item:#4a4a4a;
  --item-dark:#3a3a3a;
  --white:#fff;
  --text-dark:#222;
  --play:#1c6fd6;
  --shuffle:#c24fd6;
  --badge-accent:#6c2b9c;
}
*{box-sizing:border-box;margin:0;padding:0}
html,body{width:1029px;height:1200px;overflow:hidden}
body{background:var(--page);font-family:"Roboto",Arial,sans-serif;position:relative;color:var(--white)}
.site-header{position:absolute;left:0;top:0;width:1029px;height:86px;background:linear-gradient(#4a0a4a,var(--plum) 40%,var(--plum-dark))}
.brand{position:absolute;left:45px;top:22px;display:flex;align-items:center;gap:8px;font-size:30px;font-weight:500;color:var(--white)}
.brand-dot{width:36px;height:36px;border-radius:50%;background:var(--gold)}
.search{position:absolute;left:313px;top:26px;width:296px;height:41px;background:var(--white);border-radius:21px}
.search svg{position:absolute;right:14px;top:6px}
.header-link{position:absolute;top:28px;font-size:24px;font-weight:500;color:var(--white)}
.login{left:663px}.join{left:779px}

.side-nav{position:absolute;left:17px;top:92px;width:212px;border-radius:12px;overflow:hidden}
.side-nav a{display:block;height:42px;line-height:42px;padding-left:12px;font-size:19px;font-weight:500;color:var(--white);background:linear-gradient(#2e2e2e,#555 45%,#2a2a2a);border-bottom:1px solid #222}
.side-nav a.active{color:var(--gold)}

.moods{position:absolute;left:17px;top:227px;width:212px;border-radius:12px;overflow:hidden;background:var(--item-dark)}
.panel-head{background:linear-gradient(var(--plum-light),var(--plum) 50%,var(--plum-dark));color:var(--gold);font-size:20px;font-weight:500}
.moods .panel-head{height:43px;line-height:43px;padding-left:15px;display:flex;align-items:center;gap:12px}
.moods a{display:block;height:41.5px;line-height:41.5px;padding-left:12px;font-size:19px;font-weight:500;color:var(--white);background:linear-gradient(#505050,#3c3c3c);border-top:2px solid #333}

.hero{position:absolute;left:238px;top:92px;width:531px;height:299px;background:radial-gradient(circle at 45% 55%,#8a8a8a,#3e3e3e 60%,#1e1e1e)}
.store-badge{position:absolute;top:406px;height:43px;border-radius:5px;background:#111;border:1px solid #777}
.store-badge-accent{background:var(--badge-accent);border:none;top:409px;height:39px}

.popular-head{position:absolute;left:237px;top:466px;width:532px;height:28px;border-radius:14px 14px 0 0;text-align:center;line-height:28px}
.channels{position:absolute;left:17px;top:491px;width:752px;height:637px;background:var(--panel)}
.card{position:absolute;width:233px;height:143px;background:var(--white);color:var(--text-dark)}
.card-art{position:absolute;left:0;top:0;width:98px;height:143px;background:linear-gradient(135deg,#d8d8d8,#555 55%,#1a1a1a)}
.card-title{position:absolute;left:105px;top:0;font-size:20.5px;line-height:24px}
.card-desc{position:absolute;left:106px;top:51px;font-size:14.5px;line-height:15.5px;color:#333;width:128px}
.play{position:absolute;left:109px;top:104px;width:63px;height:26px;border:2px solid #aaa;background:linear-gradient(#3d8bf0,var(--play));color:var(--text-dark);font-size:15px;display:flex;align-items:center;gap:6px;padding-left:5px}
.shuffle{position:absolute;left:191px;top:109px}
.channels-foot{position:absolute;left:17px;top:1128px;width:533px;height:24px;border-radius:0 0 14px 14px}

.genres{position:absolute;left:778px;top:99px;width:234px;height:1059px;border-radius:16px;overflow:hidden;background:var(--item-dark)}
.genres .panel-head{height:43px;text-align:center;line-height:46px;position:relative}
.genres .panel-head::before,.genres-foot::before{content:"";position:absolute;left:18px;right:18px;top:8px;height:7px;border-radius:4px;background:#b56ab5}
.genre-list{position:relative;height:973px;overflow:hidden}
.genre-list a{display:block;height:42.4px;line-height:42.4px;padding-left:8px;width:218px;font-size:17px;color:var(--white);background:linear-gradient(#555,#3e3e3e);border-bottom:1px solid #2f2f2f}
.scrollbar{position:absolute;right:0;top:0;width:16px;height:100%;background:#2a2a2a}
.scrollbar span{display:block;margin:8px 1px 0;height:80px;background:#555}
.genres-foot{position:absolute;left:0;bottom:0;width:234px;height:43px;background:linear-gradient(var(--plum),var(--plum-dark))}
.copyright{position:absolute;left:28px;top:1183px;font-size:13px;color:var(--text-dark)}
</style>
</head>
<body>
<header class="site-header">
  <div class="brand"><span class="brand-dot"></span>TunaWave</div>
  <div class="search"><svg width="32" height="32" viewBox="0 0 32 32"><circle cx="13" cy="13" r="10" fill="none" stroke="#111" stroke-width="3"/><line x1="20" y1="20" x2="30" y2="30" stroke="#111" stroke-width="3.5"/></svg></div>
  <a class="header-link login">Log in</a>
  <a class="header-link join">Join for free!</a>
</header>

<nav class="side-nav">
  <a>My History</a><a>My Favorites</a><a class="active">Most Popular</a>
</nav>

<section class="moods">
  <div class="panel-head">Workday Moods
    <svg width="22" height="20" viewBox="0 0 22 20"><rect y="1" width="22" height="4" rx="2" fill="#f6c500"/><rect y="8" width="22" height="4" rx="2" fill="#f6c500"/><rect y="15" width="22" height="4" rx="2" fill="#f6c500"/></svg>
  </div>
  <a>Great Summer Music</a><a>Get Motivated</a><a>Concentrate</a><a>Almost 5 O’Clock</a><a>Realx and Unwind</a>
</section>

<div class="hero" role="img" aria-label="Black and white photo of headphones resting on a bag"></div>
<div class="store-badge" style="left:272px;width:103px" role="img" aria-label="App store badge"></div>
<div class="store-badge" style="left:393px;width:103px" role="img" aria-label="App store badge"></div>
<div class="store-badge" style="left:518px;width:103px" role="img" aria-label="App store badge"></div>
<div class="store-badge store-badge-accent" style="left:645px;width:99px" role="img" aria-label="Streaming device badge"></div>

<div class="popular-head panel-head">Most popular channels</div>
<section class="channels">
<div class="card" style="left:14px;top:12px"><div class="card-art" role="img" aria-label="Artist portrait"></div><div class="card-title">Magic Sunny<br>Lite Mix</div><div class="card-desc">Today's best adult hit music,some softer.</div><div class="play"><svg width="14" height="16"><polygon points="0,0 14,8 0,16" fill="#111"/></svg>Play</div><svg class="shuffle" width="22" height="16" viewBox="0 0 22 16"><path d="M1 4h5l8 8h6M1 12h5l8-8h6M17 1l3 3-3 3M17 9l3 3-3 3" fill="none" stroke="#c24fd6" stroke-width="2"/></svg></div>
<div class="card" style="left:260px;top:12px"><div class="card-art" role="img" aria-label="Artist portrait"></div><div class="card-title">Magic Sunny<br>Lite Mix</div><div class="card-desc">Today's best adult hit music,some softer.</div><div class="play"><svg width="14" height="16"><polygon points="0,0 14,8 0,16" fill="#111"/></svg>Play</div><svg class="shuffle" width="22" height="16" viewBox="0 0 22 16"><path d="M1 4h5l8 8h6M1 12h5l8-8h6M17 1l3 3-3 3M17 9l3 3-3 3" fill="none" stroke="#c24fd6" stroke-width="2"/></svg></div>
<div class="card" style="left:506px;top:12px"><div class="card-art" role="img" aria-label="Artist portrait"></div><div class="card-title">Magic Sunny<br>Lite Mix</div><div class="card-desc">Today's best adult hit music,some softer.</div><div class="play"><svg width="14" height="16"><polygon points="0,0 14,8 0,16" fill="#111"/></svg>Play</div><svg class="shuffle" width="22" height="16" viewBox="0 0 22 16"><path d="M1 4h5l8 8h6M1 12h5l8-8h6M17 1l3 3-3 3M17 9l3 3-3 3" fill="none" stroke="#c24fd6" stroke-width="2"/></svg></div>
<div class="card" style="left:14px;top:168px"><div class="card-art" role="img" aria-label="Artist portrait"></div><div class="card-title">Magic Sunny<br>Lite Mix</div><div class="card-desc">Today's best adult hit music,some softer.</div><div class="play"><svg width="14" height="16"><polygon points="0,0 14,8 0,16" fill="#111"/></svg>Play</div><svg class="shuffle" width="22" height="16" viewBox="0 0 22 16"><path d="M1 4h5l8 8h6M1 12h5l8-8h6M17 1l3 3-3 3M17 9l3 3-3 3" fill="none" stroke="#c24fd6" stroke-width="2"/></svg></div>
<div class="card" style="left:260px;top:168px"><div class="card-art" role="img" aria-label="Artist portrait"></div><div class="card-title">Magic Sunny<br>Lite Mix</div><div class="card-desc">Today's best adult hit music,some softer.</div><div class="play"><svg width="14" height="16"><polygon points="0,0 14,8 0,16" fill="#111"/></svg>Play</div><svg class="shuffle" width="22" height="16" viewBox="0 0 22 16"><path d="M1 4h5l8 8h6M1 12h5l8-8h6M17 1l3 3-3 3M17 9l3 3-3 3" fill="none" stroke="#c24fd6" stroke-width="2"/></svg></div>
<div class="card" style="left:506px;top:168px"><div class="card-art" role="img" aria-label="Artist portrait"></div><div class="card-title">Magic Sunny<br>Lite Mix</div><div class="card-desc">Today's best adult hit music,some softer.</div><div class="play"><svg width="14" height="16"><polygon points="0,0 14,8 0,16" fill="#111"/></svg>Play</div><svg class="shuffle" width="22" height="16" viewBox="0 0 22 16"><path d="M1 4h5l8 8h6M1 12h5l8-8h6M17 1l3 3-3 3M17 9l3 3-3 3" fill="none" stroke="#c24fd6" stroke-width="2"/></svg></div>
<div class="card" style="left:14px;top:324px"><div class="card-art" role="img" aria-label="Artist portrait"></div><div class="card-title">Magic Sunny<br>Lite Mix</div><div class="card-desc">Today's best adult hit music,some softer.</div><div class="play"><svg width="14" height="16"><polygon points="0,0 14,8 0,16" fill="#111"/></svg>Play</div><svg class="shuffle" width="22" height="16" viewBox="0 0 22 16"><path d="M1 4h5l8 8h6M1 12h5l8-8h6M17 1l3 3-3 3M17 9l3 3-3 3" fill="none" stroke="#c24fd6" stroke-width="2"/></svg></div>
<div class="card" style="left:260px;top:324px"><div class="card-art" role="img" aria-label="Artist portrait"></div><div class="card-title">Magic Sunny<br>Lite Mix</div><div class="card-desc">Today's best adult hit music,some softer.</div><div class="play"><svg width="14" height="16"><polygon points="0,0 14,8 0,16" fill="#111"/></svg>Play</div><svg class="shuffle" width="22" height="16" viewBox="0 0 22 16"><path d="M1 4h5l8 8h6M1 12h5l8-8h6M17 1l3 3-3 3M17 9l3 3-3 3" fill="none" stroke="#c24fd6" stroke-width="2"/></svg></div>
<div class="card" style="left:506px;top:324px"><div class="card-art" role="img" aria-label="Artist portrait"></div><div class="card-title">Magic Sunny<br>Lite Mix</div><div class="card-desc">Today's best adult hit music,some softer.</div><div class="play"><svg width="14" height="16"><polygon points="0,0 14,8 0,16" fill="#111"/></svg>Play</div><svg class="shuffle" width="22" height="16" viewBox="0 0 22 16"><path d="M1 4h5l8 8h6M1 12h5l8-8h6M17 1l3 3-3 3M17 9l3 3-3 3" fill="none" stroke="#c24fd6" stroke-width="2"/></svg></div>
<div class="card" style="left:14px;top:480px"><div class="card-art" role="img" aria-label="Artist portrait"></div><div class="card-title">Magic Sunny<br>Lite Mix</div><div class="card-desc">Today's best adult hit music,some softer.</div><div class="play"><svg width="14" height="16"><polygon points="0,0 14,8 0,16" fill="#111"/></svg>Play</div><svg class="shuffle" width="22" height="16" viewBox="0 0 22 16"><path d="M1 4h5l8 8h6M1 12h5l8-8h6M17 1l3 3-3 3M17 9l3 3-3 3" fill="none" stroke="#c24fd6" stroke-width="2"/></svg></div>
<div class="card" style="left:260px;top:480px"><div class="card-art" role="img" aria-label="Artist portrait"></div><div class="card-title">Magic Sunny<br>Lite Mix</div><div class="card-desc">Today's best adult hit music,some softer.</div><div class="play"><svg width="14" height="16"><polygon points="0,0 14,8 0,16" fill="#111"/></svg>Play</div><svg class="shuffle" width="22" height="16" viewBox="0 0 22 16"><path d="M1 4h5l8 8h6M1 12h5l8-8h6M17 1l3 3-3 3M17 9l3 3-3 3" fill="none" stroke="#c24fd6" stroke-width="2"/></svg></div>
<div class="card" style="left:506px;top:480px"><div class="card-art" role="img" aria-label="Artist portrait"></div><div class="card-title">Magic Sunny<br>Lite Mix</div><div class="card-desc">Today's best adult hit music,some softer.</div><div class="play"><svg width="14" height="16"><polygon points="0,0 14,8 0,16" fill="#111"/></svg>Play</div><svg class="shuffle" width="22" height="16" viewBox="0 0 22 16"><path d="M1 4h5l8 8h6M1 12h5l8-8h6M17 1l3 3-3 3M17 9l3 3-3 3" fill="none" stroke="#c24fd6" stroke-width="2"/></svg></div>
</section>
<div class="channels-foot panel-head"></div>

<aside class="genres">
  <div class="panel-head">Genres</div>
  <div class="genre-list">
    <a>Adult Alternative Rock</a><a>Adult Contemporary</a><a>Alt-Country</a><a>Alternative Rock</a><a>Alternative Rock Classics</a><a>Americana</a><a>Artist features</a><a>Bluegrass</a><a>Blues</a><a>Birt Rock</a><a>Broadway</a><a>Cabaret</a><a>Canadian</a><a>Celtic</a><a>Chill</a><a>Christian</a><a>Classic Rock</a><a>Classical</a><a>Comedy</a><a>Country</a><a>Dance</a><a>Decade: ‘50s</a><a>Decade: ‘60s</a>
    <div class="scrollbar"><span></span></div>
  </div>
  <div class="genres-foot"></div>
</aside>

<p class="copyright">© copyright 2014 TunaWave</p>
</body>
</html>
```